Visitenkarte erstellen für Reiki Praxis

Visitenkarten für Reiki Praxis Doppelseitig

business cards reiki practice double-sided

The background can also be a different color

```html
<!DOCTYPE html>
<html lang="en">
<head>
<meta charset="utf-8">
<title>Quiet River Wellness – Business Cards</title>
<link rel="stylesheet" href="https://fonts.googleapis.com/css2?family=Open+Sans:wght@400&family=Questrial&display=swap">
<style>
  :root {
    --backdrop: #2b2b2b;
    --paper: #ffffff;
    --ink: #050505;
    --ink-soft: #121212;
    --ink-mid: #0c0c0c;
    --text-dark: #1a1a1a;
    --text-light: #f4f4f4;
    --gold: #d7a32c;
    --gold-soft: #e0b25a;
    --rose: #c0577f;
    --pattern-top: #0b0b0b;
    --pattern-bottom: #050505;
  }
  * { box-sizing: border-box; margin: 0; padding: 0; }
  html, body {
    width: 1200px;
    height: 732px;
    overflow: hidden;
    background: var(--backdrop);
  }
  .canvas {
    position: relative;
    width: 1200px;
    height: 732px;
  }
  .card {
    position: absolute;
    top: 242px;
    width: 436px;
    height: 248px;
    overflow: hidden;
  }
  .card--front { left: 144px; background: var(--paper); }
  .card--back  { left: 621px; background: var(--ink); }

  .card__shapes {
    position: absolute;
    inset: 0;
    width: 100%;
    height: 100%;
  }

  /* Brand lockup */
  .brand {
    position: absolute;
    display: flex;
    flex-direction: column;
    align-items: center;
    gap: 8px;
  }
  .brand__dot {
    width: 30px;
    height: 30px;
    border-radius: 50%;
    background: var(--gold-soft);
  }
  .brand__name {
    font-family: "Open Sans", sans-serif;
    font-weight: 400;
    letter-spacing: 0.2px;
    white-space: nowrap;
  }
  .card--front .brand {
    left: 0;
    width: 196px;
    top: 26px;
  }
  .card--front .brand__name {
    font-size: 15px;
    color: var(--text-dark);
  }
  .card--back .brand {
    left: 0;
    right: 0;
    top: 96px;
    gap: 12px;
  }
  .card--back .brand__dot { width: 40px; height: 40px; }
  .card--back .brand__name {
    font-size: 20px;
    color: var(--text-light);
  }

  /* Contact block */
  .contact {
    position: absolute;
    right: 17px;
    top: 64px;
    text-align: right;
    color: var(--text-light);
    font-family: "Questrial", sans-serif;
  }
  .contact__name {
    font-family: "Open Sans", sans-serif;
    font-size: 15.5px;
    letter-spacing: 0.6px;
    line-height: 1.1;
  }
  .contact__role {
    font-size: 13px;
    line-height: 1.2;
    margin-top: 1px;
  }
  .contact__address {
    margin-top: 30px;
    font-size: 12.5px;
    line-height: 15px;
  }
  .contact__rule {
    width: 90px;
    height: 1.5px;
    background: var(--gold);
    margin: 9px 0 8px auto;
  }
  .contact__list { list-style: none; }
  .contact__item {
    display: flex;
    justify-content: flex-end;
    align-items: center;
    gap: 5px;
    font-size: 12.5px;
    line-height: 15px;
  }
  .contact__icon {
    width: 11px;
    height: 11px;
    flex: none;
    fill: var(--gold);
  }

  /* Back pattern area */
  .card__pattern {
    position: absolute;
    inset: 0;
    background: linear-gradient(180deg, var(--pattern-top), var(--pattern-bottom));
  }
</style>
</head>
<body>
<main class="canvas">

  <!-- Front side -->
  <section class="card card--front" aria-label="Business card front">
    <svg class="card__shapes" viewBox="0 0 895 510" preserveAspectRatio="none" aria-hidden="true">
      <defs>
        <linearGradient id="accent-diagonal" x1="0" y1="0" x2="1" y2="1">
          <stop offset="0" stop-color="#e0b25a"/>
          <stop offset="0.5" stop-color="#b9a99a"/>
          <stop offset="1" stop-color="#c0577f"/>
        </linearGradient>
        <linearGradient id="accent-base" x1="0" y1="0" x2="1" y2="0">
          <stop offset="0" stop-color="#e0b25a"/>
          <stop offset="1" stop-color="#c0577f"/>
        </linearGradient>
      </defs>
      <polygon class="panel" points="645,0 895,0 895,429 853,470 177,470" fill="var(--ink)"/>
      <polygon class="panel-facet" points="336,310 495,310 335,470 177,470" fill="var(--ink-soft)"/>
      <polygon class="panel-facet" points="416,230 480,230 400,310 336,310" fill="var(--ink-mid)"/>
      <line class="accent-diagonal" x1="615" y1="0" x2="283" y2="334" stroke="url(#accent-diagonal)" stroke-width="2.5"/>
      <line class="accent-base" x1="155" y1="490" x2="598" y2="490" stroke="url(#accent-base)" stroke-width="2.5"/>
      <line class="accent-corner" x1="870" y1="486" x2="895" y2="461" stroke="var(--gold-soft)" stroke-width="2.5"/>
    </svg>

    <div class="brand">
      <span class="brand__dot" aria-hidden="true"></span>
      <span class="brand__name">QUIET RIVER WELLNESS</span>
    </div>

    <div class="contact">
      <p class="contact__name">ELENA HARWICK</p>
      <p class="contact__role">Owner</p>
      <p class="contact__address">00 Linden Grove Lane<br>Fairhaven, FL 00000</p>
      <div class="contact__rule"></div>
      <ul class="contact__list">
        <li class="contact__item">555-014-0000
          <svg class="contact__icon" viewBox="0 0 24 24" aria-hidden="true"><path d="M6.6 10.8a15.1 15.1 0 0 0 6.6 6.6l2.2-2.2a1 1 0 0 1 1-.25 11.4 11.4 0 0 0 3.6.57 1 1 0 0 1 1 1V20a1 1 0 0 1-1 1A17 17 0 0 1 3 4a1 1 0 0 1 1-1h3.5a1 1 0 0 1 1 1c0 1.250.2 2.45.57 3.6a1 1 0 0 1-.25 1z"/></svg>
        </li>
        <li class="contact__item">elena@quietriverwellness.com
          <svg class="contact__icon" viewBox="0 0 24 24" aria-hidden="true"><path d="M2 5h20v14H2z M2 5l10 8 10-8" stroke="#000" stroke-width="1.5" stroke-linejoin="round"/></svg>
        </li>
        <li class="contact__item">www.quietriverwellness.com
          <svg class="contact__icon" viewBox="0 0 24 24" aria-hidden="true"><circle cx="12" cy="12" r="10"/><path d="M2 12h20M12 2c3 3 3 17 0 20M12 2c-3 3-3 17 0 20" stroke="#000" stroke-width="1.4" fill="none"/></svg>
        </li>
      </ul>
    </div>
  </section>

  <!-- Back side -->
  <section class="card card--back" aria-label="Business card back">
    <div class="card__pattern" role="img" aria-label="Faint repeating leaf-outline pattern in dark grey on black"></div>
    <div class="brand">
      <span class="brand__dot" aria-hidden="true"></span>
      <span class="brand__name">QUIET RIVER WELLNESS</span>
    </div>
  </section>

</main>
</body>
</html>
```